Stylish WordPress Web Site for International Young Travellers and Families

We need a WordPress Website with a stylish design for our international online registration and matching solution for Au Pairs and Host Families called Au Pair Meadow. We have strong competitors and wish to stand out with a straightforward registration process and fresh design. We need payment facilities and an easy navigation for Au Pairs and Host Families to log in, upload photos, edit their profiles etc. I need it well integrated and automation of payment receipts etc, and connected with MailChimp for newsletters etc. Logos supplied, along with website plan and text for pages. Some text to still be supplied. Can supply stock photos if required. Designer needs to advise. SIte needs to be translated into - French, Spanish, Italian, Dutch, German,

Target Market(s)

Young international travellors (aged 18-28 years) predominately female and Mums aged (28 - 48 years) of 2 or more children.

Industry/Entity Type

E-Commerce

Coding

Coded - Design and coding required

Font styles to use
Sans Serif

Requirements
Must have
• Simple registration. Great photos. Integrated with Mail Chimp. Payment facilities. Ease of log in for updating profiles, uploading photos etc. Site translated as listed above.
Nice to have
• Would love to see the compass design integrated throughout website.

```html
<!DOCTYPE html>
<html lang="en">
<head>
<meta charset="utf-8">
<title>Au Pair Meadow</title>
<link href="https://fonts.googleapis.com/css2?family=Open+Sans:ital,wght@0,400;0,600;0,700;1,400&family=Great+Vibes&display=swap" rel="stylesheet">
<style>
:root{
  --slate:#4b4862;
  --slate-dark:#3f3c54;
  --gold:#b9ad8a;
  --gold-light:#d9d2bc;
  --gold-dark:#a0966f;
  --text:#5d5d5d;
  --muted:#8a8a8a;
  --light-bg:#f3f3f6;
  --white:#ffffff;
  --footer-bar:#454545;
  --sea-top:#8fd3ea;
  --sea-mid:#3fb1d8;
  --deck:#b98a67;
}
*{box-sizing:border-box;margin:0;padding:0}
html,body{width:1200px;height:2695px;overflow:hidden;background:var(--white)}
body{font-family:"Open Sans",Arial,sans-serif;color:var(--text);position:relative}
.script{font-family:"Great Vibes",cursive;font-weight:400}
section,header,footer{position:absolute;left:0;width:1200px}

/* header */
.site-header{top:0;height:129px;z-index:3}
.header-top{position:absolute;top:0;left:0;width:1200px;height:77px;background:var(--white);border-top:4px solid var(--slate)}
.social-top{position:absolute;top:22px;left:752px;display:flex;gap:11px}
.social-top span{width:34px;height:34px;border:1.5px solid #c9c9c9;border-radius:50%}
.lang{position:absolute;top:20px;left:979px;width:136px;height:40px;border:1px solid #d3d3d3;border-radius:3px;font-size:12px;color:#444;display:flex;align-items:center;padding-left:12px;gap:8px}
.lang .flag{width:16px;height:11px;background:var(--slate)}
.lang .caret{margin-left:auto;margin-right:12px;width:0;height:0;border-left:4px solid transparent;border-right:4px solid transparent;border-top:5px solid #555}
.main-nav{position:absolute;top:77px;left:427px;width:773px;height:52px;background:var(--slate);clip-path:polygon(30px 0,100% 0,100% 100%,0 100%)}
.main-nav ul{list-style:none;display:flex;height:100%;align-items:center;padding-left:36px}
.main-nav li{color:var(--white);font-size:13px;letter-spacing:.3px;padding:0 20px;position:relative;height:100%;display:flex;align-items:center}
.main-nav li+li::before{content:"|";position:absolute;left:-2px;color:#c9c6d6}
.main-nav li.active{background:var(--gold)}
.logo{position:absolute;top:0;left:81px;width:252px;height:180px;background:var(--white);border-radius:0 0 126px 126px / 0 0 70px 70px;display:flex;flex-direction:column;align-items:center;justify-content:center;gap:10px;padding-top:10px}
.logo .dot{width:30px;height:30px;border-radius:50%;background:var(--gold)}
.logo .name{font-size:24px;font-weight:600;color:var(--slate);letter-spacing:.3px}

/* hero */
.hero{top:77px;height:537px;background:linear-gradient(180deg,var(--sea-top) 0%,var(--sea-mid) 55%,#6ec4df 72%,var(--deck) 100%)}
.hero-photo{position:absolute;inset:0}
.hero-copy{position:absolute;left:84px;top:210px;width:480px;color:var(--white)}
.hero-copy h1{font-size:52px;line-height:1;margin-bottom:18px}
.hero-copy p{font-size:12px;font-style:italic;line-height:22px;opacity:.92}
.btn-dark{display:inline-block;margin-top:36px;width:144px;height:47px;line-height:47px;text-align:center;background:var(--slate);color:var(--white);font-size:13px}
.slider-dots{position:absolute;top:501px;left:557px;display:flex;gap:5px}
.slider-dots span{width:13px;height:13px;border:1.5px solid var(--white);border-radius:50%}
.slider-dots span.on{background:var(--white)}

/* about */
.about{top:614px;height:338px;background:var(--white)}
.compass-art{position:absolute;left:72px;top:46px;width:377px;height:229px;background:radial-gradient(circle at 50% 50%,#d9dbe6 0,#eceef3 45%,#ffffff 72%)}
.section-title{font-size:38px;color:var(--slate);line-height:1}
.section-title em{font-style:normal;color:var(--gold)}
.about .section-title{position:absolute;left:453px;top:40px}
.about-text{position:absolute;left:453px;top:100px;width:640px;font-size:12.5px;line-height:25px}
.about-text p+p{margin-top:15px}

/* titles with ornament spot */
.titled{display:flex;align-items:center;gap:14px}
.ornament{width:52px;height:52px;border-radius:50%;background:radial-gradient(circle,#ffffff 0,#d7d5df 100%)}

/* testimonials */
.testimonials{top:952px;height:410px;background:linear-gradient(180deg,var(--gold-light) 0%,#c9c0a2 50%,var(--gold-dark) 100%)}
.testimonials .titled{position:absolute;top:30px;left:0;width:1200px;justify-content:center}
.testimonials .section-title{color:var(--white)}
.quote{position:absolute;top:113px;width:476px;height:151px;background:var(--white);padding:18px 24px;font-size:12px;font-style:italic;line-height:24px;color:var(--text)}
.quote::after{content:"";position:absolute;bottom:-18px;left:70px;border-left:0 solid transparent;border-right:22px solid transparent;border-top:18px solid var(--white)}
.quote .mark{font-style:normal;font-weight:700;font-size:20px;color:#888;vertical-align:-4px;margin-right:4px}
.q1{left:86px}.q2{left:638px}
.author{position:absolute;top:284px;display:flex;align-items:center;gap:36px}
.a1{left:108px}.a2{left:632px}
.avatar{width:82px;height:82px;border-radius:50%;border:4px solid var(--white);background:linear-gradient(135deg,#9aa3b3,#6b6e7e)}
.author .who{color:var(--white)}
.author .who .nm{font-size:25px;line-height:1.1}
.author .who .sub{font-size:11px;margin-top:4px}

/* how it works */
.how{top:1362px;height:416px;background:var(--light-bg)}
.how .titled{position:absolute;top:30px;left:0;width:1200px;justify-content:center}
.step{position:absolute;top:143px;width:245px;height:243px;background:var(--white);border:1px solid #e3e3e8;text-align:center;padding:0 18px}
.step .num{position:absolute;top:-38px;left:72px;width:100px;height:100px;border-radius:50%;background:var(--white);border:6px solid #eceaf0;display:flex;align-items:center;justify-content:center;font-size:40px;color:var(--slate)}
.step h3{margin-top:70px;font-size:28px;color:var(--slate);line-height:1}
.step p{margin-top:14px;font-size:11.5px;line-height:23px;color:var(--text)}
.step.active{background:var(--slate);border-color:var(--slate)}
.step.active .num{background:var(--slate);border-color:var(--white);color:var(--white)}
.step.active h3,.step.active p{color:var(--white)}
.s1{left:86px}.s2{left:347px}.s3{left:609px}.s4{left:871px}

/* why */
.why{top:1778px;height:365px;background:var(--white)}
.why .titled{position:absolute;left:86px;top:34px}
.why-text{position:absolute;left:86px;top:112px;width:560px;font-size:12px;font-style:italic;line-height:25px}
.why-text p+p{margin-top:15px}
.read-more{position:absolute;left:86px;top:307px;font-size:12px;font-weight:600;color:var(--slate);text-decoration:underline}
.why-photo{position:absolute;left:691px;top:43px;width:423px;height:280px;border:6px solid var(--white);box-shadow:0 0 0 1px #dcdcdc;background:linear-gradient(180deg,#cfe3e2 0%,#a9c9c8 50%,#e6c7b4 100%)}

/* audience band */
.audience{top:2143px;height:197px;background:var(--slate)}
.audience .left-bg{position:absolute;inset:0;background:var(--gold);clip-path:polygon(0 0,557px 0,647px 100%,0 100%)}
.aud-col{position:absolute;top:34px;width:480px;color:var(--white)}
.aud-col .titled{gap:10px}
.aud-col .ornament{width:42px;height:42px}
.aud-col h2{font-size:34px;line-height:1;color:var(--white)}
.aud-col p{margin-top:12px;font-size:11.5px;font-style:italic;line-height:22px}
.btn-line{display:inline-block;margin-top:16px;width:112px;height:40px;line-height:38px;text-align:center;border:1.5px solid var(--white);font-size:13px;letter-spacing:.4px}
.c-left{left:86px}.c-right{left:665px}

/* footer */
.site-footer{top:2340px;height:286px;background:var(--white)}
.foot-logo{position:absolute;left:108px;top:58px;width:224px;height:171px;display:flex;flex-direction:column;align-items:center;justify-content:center;gap:12px}
.foot-logo .dot{width:34px;height:34px;border-radius:50%;background:var(--gold)}
.foot-logo .name{font-size:24px;font-weight:600;color:var(--slate)}
.foot-col{position:absolute;top:64px}
.foot-col h4{font-size:15px;font-weight:600;color:#444;letter-spacing:.3px;margin-bottom:20px}
.contact{left:366px;width:220px}
.contact li{list-style:none;display:flex;align-items:flex-start;gap:14px;font-size:12px;color:var(--text);margin-bottom:12px;line-height:17px}
.contact svg{flex:none;margin-top:2px}
.contact a{color:var(--text)}
.newsletter{left:632px;width:220px}
.newsletter p{font-size:12px;line-height:19px;color:var(--text)}
.field{margin-top:16px;width:213px;height:35px;border:1px solid #d8d8d8;font-size:11px;color:#777;padding:10px 14px}
.subscribe{margin-top:10px;width:80px;height:26px;background:var(--gold);color:var(--white);font-size:10px;text-align:center;line-height:26px}
.follow{left:885px;width:230px}
.follow p{font-size:11.5px;line-height:19px;color:var(--text)}
.follow .circles{display:flex;gap:9px;margin-top:24px}
.follow .circles span{width:36px;height:36px;border-radius:50%;border:1.5px solid #c6c6c6}
.copyright{top:2626px;height:69px;background:var(--footer-bar);color:var(--white);font-size:12px;text-align:center;line-height:69px}
</style>
</head>
<body>

<header class="site-header">
  <div class="header-top">
    <div class="social-top"><span></span><span></span><span></span><span></span><span></span></div>
    <div class="lang"><span class="flag"></span>English<span class="caret"></span></div>
  </div>
  <nav class="main-nav">
    <ul>
      <li class="active">HOME</li>
      <li>ABOUT US</li>
      <li>SERVICES</li>
      <li>HOW DOES IT WORK?</li>
      <li>NEWS</li>
      <li>CONTACT US</li>
    </ul>
  </nav>
  <div class="logo"><span class="dot"></span><span class="name">Au Pair Meadow</span></div>
</header>

<section class="hero">
  <div class="hero-photo" role="img" aria-label="Photo of a family with two children running along a sunny pier by the sea with luggage"></div>
  <div class="hero-copy">
    <h1 class="script">Au Pair Meadow</h1>
    <p>Keeping your world and the little people in it happy, is no easy task.  Some times that washing pile never gets smaller and wouldn't it be just great knowing that when you get home from work, that dinner is already on the be a more balanced, we all need a little help.</p>
    <span class="btn-dark">READ MORE</span>
  </div>
  <div class="slider-dots"><span></span><span></span><span class="on"></span><span></span><span></span></div>
</section>

<section class="about">
  <div class="compass-art" role="img" aria-label="Large decorative compass rose"></div>
  <h2 class="section-title script">About <em>Au Pair Meadow</em></h2>
  <div class="about-text">
    <p>Keeping your world and the little people in it happy, is no easy task.  Sometimes that washing pile never gets smaller and wouldn't it be just great knowing that when you get home from work, that dinner is already on the table, the kids feed, bathed and dressed for bed.We get it. Life is busy.  a  some time to get to the gym and maybe just to be a more balanced, we all need a little help.</p>
    <p>You can find your Meadow Au Pair, they are a person between the age of 18 and 30 years of age with various skills and experience to join you in your home.  Often they are students taking a break from study to travel abroad. They are keen care for your children in exchange for full board and pocket money.</p>
  </div>
</section>

<section class="testimonials">
  <div class="titled"><span class="ornament" role="img" aria-label="Small compass ornament"></span><h2 class="section-title script">Our Testimonials</h2></div>
  <blockquote class="quote q1"><span class="mark">&ldquo;</span>I have been an Au Pair twice now, both with amazing families who have treated me like their daughter.  The experience is unique and has given me the opportunity to travel affordably and practise my English.  I love children and this is important, I love cooking and my families loved the meals I prepared......</blockquote>
  <blockquote class="quote q2"><span class="mark">&ldquo;</span>I have been an Au Pair twice now, both with amazing families who have treated me like their daughter.  The experience is unique and has given me the opportunity to travel affordably and practise my English.  I love children and this is important, I love cooking and my families loved the meals I prepared......</blockquote>
  <div class="author a1">
    <span class="avatar" role="img" aria-label="Portrait photo of the au pair"></span>
    <div class="who"><div class="nm script">Lina Moreau - Au Pair</div><div class="sub">(aged 20 years, from France)</div></div>
  </div>
  <div class="author a2">
    <span class="avatar" role="img" aria-label="Portrait photo of the host mum"></span>
    <div class="who"><div class="nm script">Hannah Riley - Host Mum</div><div class="sub">3 children aged 18months to 8 years old</div></div>
  </div>
</section>

<section class="how">
  <div class="titled"><span class="ornament" role="img" aria-label="Small compass ornament"></span><h2 class="section-title script">How Does <em>It Work</em></h2></div>
  <div class="step s1 active"><span class="num script">01</span><h3 class="script">Step</h3><p>All that is required is a straightforward free registration and enter your search criteria and your ideal candidates profiles will be displayed.</p></div>
  <div class="step s2"><span class="num script">02</span><h3 class="script">Step</h3><p>Once you have selected your choices you can send a secure message to discuss details further including inter perfect Au Pair or Host Family.</p></div>
  <div class="step s3"><span class="num script">03</span><h3 class="script">Step</h3><p>Au Pairs book their travel in and Host Families prepare to welcome you into their home.</p></div>
  <div class="step s4"><span class="num script">04</span><h3 class="script">Step</h3><p>Once your have made your choice you can choose to make you profile inactive and easily reinstate it again when you are being searching again.</p></div>
</section>

<section class="why">
  <div class="titled"><span class="ornament" role="img" aria-label="Small compass ornament"></span><h2 class="section-title script">Why Au Pair <em>Meadow is for you?</em></h2></div>
  <div class="why-text">
    <p>We believe in the product – that's right you!  Walter Dane said it well, "Do what you do so well that they will want to see it again and bring their friends." Creating love between you and Au Pair Meadow will provide positive word of mouth and that's absolutely priceless.</p>
    <p>We know that our platform.  It is the most modern and sophisticated and offers Au Pairs and Families the best solution and greatest of opportunities. We have experience – we are the Au Pairs and we are the experience ourselves of what makes it work and the exciting benefits to both parties.</p>
  </div>
  <span class="read-more">READ MORE INFO</span>
  <div class="why-photo" role="img" aria-label="Photo of a smiling family with two children walking through an airport with luggage"></div>
</section>

<section class="audience">
  <div class="left-bg"></div>
  <div class="aud-col c-left">
    <div class="titled"><span class="ornament" role="img" aria-label="Small compass ornament"></span><h2 class="script">Au Pairs</h2></div>
    <p>We know that our platform.  It is the most modern and sophisticated and offers Au Pairs and Families the best solution and greatest of opportunities.</p>
    <span class="btn-line">SIGN UP</span>
  </div>
  <div class="aud-col c-right">
    <div class="titled"><span class="ornament" role="img" aria-label="Small compass ornament"></span><h2 class="script">Host Families</h2></div>
    <p>We know that our platform.  It is the most modern and sophisticated and offers Au Pairs and Families the best solution and greatest of opportunities.</p>
    <span class="btn-line">SIGN UP</span>
  </div>
</section>

<footer class="site-footer">
  <div class="foot-logo"><span class="dot"></span><span class="name">Au Pair Meadow</span></div>
  <div class="foot-col contact">
    <h4>CONTACT US</h4>
    <ul>
      <li><svg width="14" height="12" viewBox="0 0 14 12"><path d="M1 4c0-2 3-3 6-3s6 1 6 3l-2 1-1-2H4L3 5z M3 6h8l1 5H2z" fill="#666"/></svg>(000)-121-1231 (Phone)</li>
      <li><svg width="14" height="12" viewBox="0 0 14 12"><rect x="3" y="0" width="8" height="4" fill="#666"/><rect x="1" y="4" width="12" height="5" fill="#666"/><rect x="3" y="8" width="8" height="4" fill="#999"/></svg>(000)-121-1231 (Fax)</li>
      <li><svg width="14" height="10" viewBox="0 0 14 10"><rect width="14" height="10" fill="#666"/><path d="M0 0l7 5 7-5" stroke="#fff" fill="none"/></svg><a>info@aupairmeadow.com</a></li>
      <li><svg width="14" height="14" viewBox="0 0 14 14"><path d="M7 0a5 5 0 0 1 5 5c0 4-5 9-5 9S2 9 2 5a5 5 0 0 1 5-5z" fill="#666"/><circle cx="7" cy="5" r="2" fill="#fff"/></svg># 356 Lorem Ipsum Dummy Lorem ipsum</li>
    </ul>
  </div>
  <div class="foot-col newsletter">
    <h4>NEWSLETTER</h4>
    <p>Register Your email address to get information ablout us</p>
    <div class="field">Email Address</div>
    <div class="subscribe">SUBSCRIBE</div>
  </div>
  <div class="foot-col follow">
    <h4>FOLLOW US</h4>
    <p>Lorem ipsum dolor sit amet, conse ctetur adipiscing elit. Nulla in purus nibh. Donec ornare</p>
    <div class="circles"><span></span><span></span><span></span><span></span><span></span></div>
  </div>
</footer>

<div class="copyright" style="position:absolute;left:0;width:1200px">© Copyright 2016 Au Pair Meadow .All Rights Reserved</div>

</body>
</html>
```